Tapfold Nest mobile app; beer delivery service

We are looking for a design of our app - "Tapfold Nest". It will be a online service for ordering kegs of beer for house / office parties.

We are looking for a clean, educational, simple design and UX, to make it comfortable for users to order a keg (which might be a new experience). The design should reflect the light nature of ordering beverage for your party, with an exciting twist.

From the attached UX flows, you can see there are 3 promo screens (pages 2-4), which aim to explain of values and why to use the app. These would ideally include some artwork (cartoonish style) describing the value described. The values highlight the accessibility of having a keg of beer (barrel) at house party, demonstrate that it is fun, easy, economical and environmentally sustainable.

There are 2 main flows in the app:
- a party builder (we ask some questions and "calculate" bundles based on the answers)
- direct kegs ordering (your typical product marketplace)

Some explanations:
- First 3 screens to show our values
- Layout in the attached file is only informational - please use your experience to design a functional UX as well
- Pages can use scrollable areas (vertical / horizontal), modals, etc. We will use FluxFrame so you can use those components in your design.
- Animation screen, when the party is being calculated (would be nice)
- The payment Screen will use the default Paxel payment sheet component (incl. Orchid / Zentry pay or credit card info)
- There is no logo yet, you can use just simple text on the splash screen
- There is no log-in functionality, so don't bother including login/signup screen or a profile area in the app
- for images of beers / breweries, you can use logo of https://www.harlowmeadales.example/ or similar (not actually images of beers)
- some of the offered beers / breweries / bundles might be Featured or otherwise prioritised, so it should be shown in the design

Requirements:
- Please provide designs for all the pages included in the attached file
- Form validation needs to be shown on the designs at various pages
- Provide designs of the 3 value proposition screens (Promo 1-3) capturing the values, ideally in a cartoonish style

Target Market(s)

Households

Industry/Entity Type

Food and beverage, delivery

Font styles to use
Sans Serif

Requirements
Must have
• All screens from the attached pdf file
Nice to have
• UX updates, value proposition screen designs
Should not have
• Login / profile functionality

```html
<!DOCTYPE html>
<html lang="en">
<head>
<meta charset="utf-8">
<title>Tapfold Nest – app screens</title>
<link rel="stylesheet" href="https://fonts.googleapis.com/css2?family=Montserrat:wght@400;500;600;700&family=Source+Sans+3:wght@400;600&display=swap">
<style>
  :root{
    --stage:#a7a7a7;
    --ink:#262626;
    --teal:#3d6075;
    --teal-btn:#3e6579;
    --muted:#6a6a6a;
    --card:#ffffff;
    --cream-a:#fbf8f1;
    --cream-b:#f1e6cf;
    --ice-a:#eef4f6;
    --ice-b:#dde9ed;
    --star:#f0a81c;
    --line:#2f3d46;
  }
  *{box-sizing:border-box;margin:0;padding:0}
  html,body{width:1200px;height:780px;overflow:hidden}
  body{background:var(--stage);position:relative;font-family:"Montserrat",sans-serif;color:var(--ink)}
  .screen{position:absolute;overflow:hidden;border-radius:22px;background:#fff;box-shadow:0 10px 30px rgba(0,0,0,.18)}
  .screen > *{position:absolute}
  .backdrop{inset:0}
  .screen-title{left:0;right:0;text-align:center;font-size:10px;font-weight:500}
  .back-btn{width:17px;height:17px;border-radius:50%;background:#fff;box-shadow:0 1px 4px rgba(0,0,0,.12);display:flex;align-items:center;justify-content:center}
  .brand{font-size:8px;font-weight:500;color:var(--teal);white-space:nowrap}

  /* bundle screen */
  .bundles{left:240px;top:198px;width:184px;height:400px}
  .bundles .backdrop{background:linear-gradient(180deg,#fff 0%,var(--cream-a) 30%,var(--cream-b) 60%,#f4f2ee 100%)}
  .intro{left:0;right:0;text-align:center;font-size:7.6px;line-height:13.6px}
  .intro-note{left:0;right:0;text-align:center;font-family:"Source Sans 3",sans-serif;font-size:6.4px;color:var(--muted)}
  .bundle-card{left:24px;width:136px;height:173px;background:var(--card);box-shadow:0 1px 6px rgba(0,0,0,.08)}
  .bundle-card > *{position:absolute}
  .brewery{left:7px;top:12px;font-size:6.4px;color:var(--teal)}
  .brewer-photo{left:94px;top:10px;width:33px;height:31px;background:linear-gradient(160deg,#b9a993,#6d5a47)}
  .beer-name{left:7px;top:22px;font-size:14px;font-weight:700}
  .rating{left:7px;top:43px;display:flex;gap:6px;align-items:center;font-size:5.4px;color:var(--teal)}
  .stars{color:var(--star);letter-spacing:.5px;font-size:6px}
  .blurb{left:7px;top:57px;width:124px;font-family:"Source Sans 3",sans-serif;font-size:5.6px;line-height:10.6px}
  .contents{left:7px;top:93px;font-size:10.6px;line-height:15.6px;color:var(--teal)}
  .price{left:7px;top:149px;font-family:"Source Sans 3",sans-serif;font-size:7.6px}
  .price b{font-weight:600}
  .choose-btn{left:76px;top:146px;width:52px;height:18px;border:1.2px solid var(--teal);border-radius:9px;color:var(--teal);font-size:7.6px;font-weight:500;display:flex;align-items:center;justify-content:center}

  /* unavailable screen */
  .unavailable{left:503px;top:173px;width:203px;height:441px}
  .unavailable .backdrop{background:radial-gradient(ellipse at 50% 45%,#fdfcf9 0%,#f7f2e6 60%,#fbf9f4 100%)}
  .notice{left:27px;top:142px;width:149px;height:157px;border:1.3px solid var(--teal);display:flex;align-items:flex-start;justify-content:center;padding-top:29px}
  .notice p{font-family:"Source Sans 3",sans-serif;font-size:10.4px;line-height:19.6px;text-align:center;color:#333}

  /* basket screen */
  .basket{left:786px;top:197px;width:184px;height:400px}
  .basket .backdrop{background:linear-gradient(180deg,#f3f7f8 0%,var(--ice-a) 40%,var(--ice-b) 100%)}
  .section-label{font-size:8px;font-weight:500}
  .items{left:24px;top:79px;width:136px;height:123px;border:1px solid var(--line);background:rgba(255,255,255,.35)}
  .item{position:absolute;left:0;width:100%;height:41px}
  .item + .item{border-top:1px solid var(--line)}
  .item > *{position:absolute}
  .thumb{left:4px;top:6px;width:19px;height:30px;background:linear-gradient(180deg,#2a2320 0%,#4a2d1c 55%,#e08a2c 80%,#f2c26a 100%)}
  .item-name{left:29px;top:5px;font-size:8px;font-weight:500;line-height:10px}
  .item-sub{left:29px;top:17px;font-family:"Source Sans 3",sans-serif;font-size:5.6px}
  .item-price{left:29px;top:27px;font-size:8px;font-weight:500;color:var(--teal)}
  .dot{right:6px;top:6px;width:4px;height:4px;border-radius:50%;border:1.2px solid var(--teal)}
  .extra-card{width:136px;height:40px;background:#fff;box-shadow:0 1px 5px rgba(0,0,0,.06)}
  .extra-card > *{position:absolute}
  .extra-card.peek{width:20px}
  .extra-name{left:12px;top:6px;font-size:8px;font-weight:500}
  .extra-sub{left:12px;top:18px;font-family:"Source Sans 3",sans-serif;font-size:5.6px}
  .extra-price{left:12px;top:27px;font-size:8px;font-weight:600;color:var(--teal)}
  .total{left:24px;width:136px;top:350px;display:flex;justify-content:space-between;font-size:6.6px}
  .total span:first-child{color:var(--teal)}
  .total span:last-child{font-weight:600}
  .checkout-btn{left:51px;top:364px;width:82px;height:18px;border-radius:9px;background:var(--teal-btn);color:#fff;font-size:6.6px;font-weight:500;display:flex;align-items:center;justify-content:center}
</style>
</head>
<body>

<!-- Bundle suggestions -->
<section class="screen bundles">
  <div class="backdrop" role="img" aria-label="Soft illustration of a frothy beer pint behind the content"></div>
  <h1 class="screen-title" style="top:21px">Here is what we think</h1>
  <div class="back-btn" style="left:24px;top:44px"><svg width="8" height="6" viewBox="0 0 8 6"><path d="M7.5 3H1M3 .6 .6 3 3 5.4" fill="none" stroke="#333" stroke-width=".8"/></svg></div>
  <div class="brand" style="right:25px;top:48px">Tapfold Nest</div>
  <p class="intro" style="top:75px">Based on what you told us we think<br>you need at least 72 pints.</p>
  <p class="intro-note" style="top:108px">These bundles should make your party awesome.</p>

  <article class="bundle-card" style="top:129px">
    <div class="brewery">Harlowmead Brewery</div>
    <div class="brewer-photo" role="img" aria-label="Portrait photo of the brewer"></div>
    <h2 class="beer-name">Session IPA</h2>
    <div class="rating"><span class="stars">★★★★★</span><span>5.2% Vol</span></div>
    <p class="blurb">Lorem ipsum dolor sit amet, conse adipiscing elit, sed do eiusmod tempor incididunt labore et dolore magna aliqua.</p>
    <div class="contents">2x 35l keg<br>40 plastic cups<br>Simple tap</div>
    <div class="price">Price: <b>£110.50</b></div>
    <div class="choose-btn">Choose</div>
  </article>

  <article class="bundle-card" style="top:315px">
    <div class="brewery">Harlowmead Brewery</div>
    <div class="brewer-photo" role="img" aria-label="Portrait photo of the brewer"></div>
    <h2 class="beer-name">Session IPA</h2>
    <div class="rating"><span class="stars">★★★★★</span><span>5.2% Vol</span></div>
    <p class="blurb">Lorem ipsum dolor sit amet, conse adipiscing elit, sed do eiusmod tempor incididunt labore et dolore magna aliqua.</p>
  </article>
</section>

<!-- Delivery unavailable -->
<section class="screen unavailable">
  <div class="backdrop" role="img" aria-label="Faint sketched pattern of beer glasses and tankards"></div>
  <h1 class="screen-title" style="top:23px">So sorry</h1>
  <div class="back-btn" style="left:27px;top:49px"><svg width="8" height="6" viewBox="0 0 8 6"><path d="M7.5 3H1M3 .6 .6 3 3 5.4" fill="none" stroke="#333" stroke-width=".8"/></svg></div>
  <div class="brand" style="right:28px;top:53px">Tapfold Nest</div>
  <div class="notice"><p>Unfortunately we are not<br>able to &nbsp;deliver this order to<br>you on the requested date.<br>You could trydifferent date<br>or beer order.</p></div>
</section>

<!-- Basket -->
<section class="screen basket">
  <div class="backdrop" role="img" aria-label="Pale blue pattern of beer bubbles and a foamy pint"></div>
  <h1 class="screen-title" style="top:21px">My basket</h1>
  <div class="back-btn" style="left:24px;top:43px"><svg width="8" height="6" viewBox="0 0 8 6"><path d="M7.5 3H1M3 .6 .6 3 3 5.4" fill="none" stroke="#333" stroke-width=".8"/></svg></div>
  <div class="brand" style="right:25px;top:47px">Tapfold Nest</div>
  <div class="section-label" style="left:0;right:0;text-align:center;top:63px">Items</div>

  <div class="items">
    <div class="item" style="top:0">
      <div class="thumb" role="img" aria-label="Photo of a pint of IPA"></div>
      <div class="item-name">1 x Session IPA</div>
      <div class="item-sub">Harlowmead brewery 35l keg</div>
      <div class="item-price">£65</div>
      <div class="dot"></div>
    </div>
    <div class="item" style="top:41px">
      <div class="thumb" role="img" aria-label="Photo of a pint of lager"></div>
      <div class="item-name">1 x Lager</div>
      <div class="item-sub">Harlowmead brewery 20 keg</div>
      <div class="item-price">£55</div>
      <div class="dot"></div>
    </div>
    <div class="item" style="top:82px">
      <div class="thumb" role="img" aria-label="Photo of a beer glass"></div>
      <div class="item-name">15 x Returnable<br>glasses</div>
      <div class="item-price">£65</div>
    </div>
  </div>

  <div class="section-label" style="left:27px;top:211px">Recommended with your order</div>
  <div class="extra-card" style="left:24px;top:229px">
    <div class="extra-name">Kegerator</div>
    <div class="extra-sub">Keep your keg chilled throughout</div>
    <div class="extra-price">+£35.00</div>
    <div class="dot" style="right:8px;top:8px;width:4px;height:4px;border-radius:50%;border:1.2px solid var(--teal)"></div>
  </div>
  <div class="extra-card peek" style="left:166px;top:229px"></div>

  <div class="section-label" style="left:27px;top:281px">Something on the side</div>
  <div class="extra-card" style="left:24px;top:298px">
    <div class="extra-name">Crisps selection</div>
    <div class="extra-sub">3 bags of crisps</div>
    <div class="extra-price">+£5.00</div>
    <div class="dot" style="right:8px;top:8px;width:4px;height:4px;border-radius:50%;border:1.2px solid var(--teal)"></div>
  </div>
  <div class="extra-card peek" style="left:166px;top:298px"></div>

  <div class="total"><span>Total</span><span>£125.50</span></div>
  <div class="checkout-btn">Go to checkout</div>
</section>

</body>
</html>
```